Bargain Haven marketing postcard

We are a nonprofit that runs a thrift store to fund our mission. Our mission is to create jobs and independence for people with long term serious mental illnesses. We recently purchased a cargo van for neighborhood pickups and we want to publicize our services. We accept donations of furniture, clothing, electronics, art, and other household items. We are a 501(c)(3) and all donations are potentially tax deductible. We have a logo that is attached below. The phone to call for pickup: (301) 738-7723Our websites: www.brightpathworksinc.org, www.maplecornerthriftshop.org

Target Market(s)

Potential donors

Industry/Entity Type

Marketing

Font styles to use
Serif
Sans Serif

Requirements
Must have
• We are rebranding so I would like to have the new name of the store: Bargain Haven. Also reference to the old name (formerly Maple Corner Thrift Shop). I'd like it to say that it is "a project of Brightpath Works, Inc." and that we are a 501(c)(3). Finally, please mention that we do in-home donation pick-up and provide the contact number.

```html
<!DOCTYPE html>
<html lang="en">
<head>
<meta charset="utf-8">
<title>Bargain Haven – Donation Pickup Postcard</title>
<link rel="stylesheet" href="https://fonts.googleapis.com/css2?family=Arimo:wght@400;700&family=Roboto:wght@300;400;700&display=swap">
<style>
  :root {
    --olive: #b7b489;
    --ink: #111111;
    --body-grey: #5f5e55;
    --mid-grey: #333333;
    --soft-grey: #666666;
    --rule-green: #a9bea0;
    --paper: #ffffff;
    --back-band: #f7f7f5;
    --lotus-dark: #6f7a2e;
    --lotus-light: #d9d6a8;
  }
  * { margin: 0; padding: 0; box-sizing: border-box; }
  html, body {
    width: 1200px; height: 503px; overflow: hidden;
    background: var(--paper);
  }
  .canvas { position: relative; width: 1200px; height: 503px; font-family: "Arimo", Arial, sans-serif; }

  /* Front — left panel */
  .front-left {
    position: absolute; left: 0; top: 0; width: 334px; height: 449px;
    background: var(--olive);
  }
  .brand-name {
    position: absolute; left: 40px; top: 24px;
    font-weight: 400; font-size: 24px; color: var(--mid-grey);
  }
  .brand-note {
    position: absolute; left: 40px; right: 10px; top: 55px;
    font-size: 10.5px; line-height: 13px; color: var(--mid-grey);
  }
  .front-left .headline {
    position: absolute; left: 0; right: 0; top: 97px; text-align: center;
    font-weight: 700; font-size: 21px; color: var(--ink);
  }
  .front-left .copy {
    position: absolute; left: 6px; right: 4px; top: 146px;
    font-family: "Roboto", Arial, sans-serif; font-weight: 300;
    font-size: 12.2px; line-height: 16.3px; color: var(--body-grey);
  }
  .front-left .copy p { margin-bottom: 12px; }
  .front-left .copy strong { font-weight: 700; color: var(--ink); }

  /* Front — middle panel */
  .front-mid {
    position: absolute; left: 334px; top: 0; width: 275px; height: 449px;
    text-align: center; color: var(--ink);
  }
  .shop-open { margin-top: 5px; font-size: 20px; font-weight: 400; }
  .hours { margin-top: 6px; font-size: 13.2px; line-height: 16.4px; }
  .rule { position: absolute; left: 22px; width: 229px; height: 3px; background: var(--rule-green); }
  .rule.top { top: 133px; }
  .rule.bottom { top: 239px; }
  .ways {
    position: absolute; left: 0; right: 0; top: 140px;
    font-size: 14.6px; line-height: 18px; font-weight: 700;
  }
  .contact {
    position: absolute; left: 0; right: 0; top: 180px;
    font-size: 14px; line-height: 18px;
  }
  .lotus { position: absolute; left: 52px; top: 266px; width: 142px; height: 138px; }
  .mission {
    position: absolute; left: 28px; right: 50px; top: 338px;
    font-family: "Roboto", Arial, sans-serif; font-weight: 300;
    font-size: 13px; line-height: 17px; color: var(--soft-grey);
  }

  /* Back */
  .back {
    position: absolute; left: 612px; top: 0; width: 588px; height: 449px;
    border: 2px solid var(--ink); background: var(--paper);
  }
  .back-band {
    position: absolute; left: 34px; top: 0; width: 430px; height: 126px;
    background: var(--back-band);
  }
  .back-title {
    position: absolute; left: 0; width: 460px; top: 4px; text-align: center;
    font-weight: 700; font-size: 27px; line-height: 33px; color: var(--ink);
  }
  .back-contact {
    position: absolute; left: 0; width: 440px; top: 74px; text-align: center;
    font-size: 16px; line-height: 19.5px; color: var(--ink);
  }

  .side-label { position: absolute; top: 474px; font-weight: 700; font-size: 18px; color: var(--ink); }
  .side-label.front { left: 507px; }
  .side-label.back-label { left: 636px; }
</style>
</head>
<body>
<main class="canvas">
  <section class="front-left">
    <div class="brand-name">Bargain Haven</div>
    <div class="brand-note">formerly Maple Corner Thrift Shop<br>A project of Brightpath Works, Inc., a 501(c)(3)</div>
    <h1 class="headline">We Can Pick Up Donations!</h1>
    <div class="copy">
      <p>Bargain Haven generally runs Tuesday - Saturday, and we'll go anywhere in the DC Metro area for good furniture. When coming out for clothing and other small items, we usually schedule it on a day when we'll already be in that neighborhood.</p>
      <p>Clothes, books, household goods, and other small items should be ready for our truck in a bag or a box. You do not need to bring your donations to the curb. <strong>We'll be happy to pick up boxes, bags, and furniture from wherever you have them in your home.</strong></p>
      <p>All donations should be in good to excellent condition. We're a bit more lenient in terms of condition when it comes to nice wood furniture. Conversely, we're less lenient when it comes to upholstered furniture (we do NOT accept couches and other upholstered furniture in mediocre condition, even if it's otherwise perfectly usable).</p>
    </div>
  </section>

  <section class="front-mid">
    <h2 class="shop-open">Our Shop is Open!</h2>
    <div class="hours">Hours<br>Mon-Thurs: 10am-pm<br>Fri-Sat: 10am-7pm<br>Sun: Noon-5pm</div>
    <div class="rule top"></div>
    <div class="ways">2 Easy Ways<br>We Can Pick Up Donations!</div>
    <div class="contact">Call: (555) 214-9086<br>or Visit Our Website:<br>www.maplecornerthriftshop.org</div>
    <div class="rule bottom"></div>
    <svg class="lotus" role="img" aria-label="Decorative lotus blossom ornament in olive tones" viewBox="0 0 142 138">
      <defs>
        <linearGradient id="lotusFill" x1="0" y1="0" x2="0" y2="1">
          <stop offset="0" stop-color="#6f7a2e"/>
          <stop offset="1" stop-color="#d9d6a8" stop-opacity="0.4"/>
        </linearGradient>
      </defs>
      <ellipse cx="71" cy="69" rx="70" ry="68" fill="url(#lotusFill)"/>
    </svg>
    <p class="mission">We are a nonprofit that runs a thrift store to fund our mission. Our mission is to create jobs and independence for people with long term serious mental illnesses.</p>
  </section>

  <section class="back">
    <div class="back-band"></div>
    <h2 class="back-title">2 Easy Ways<br>We Can Pick Up Donations!</h2>
    <div class="back-contact">Call: (555) 214-9086<br>or Visit Our Website:<br>www.maplecornerthriftshop.org</div>
  </section>

  <div class="side-label front">front</div>
  <div class="side-label back-label">back</div>
</main>
</body>
</html>
```